Refrigeration & Air Conditioning modern and appealing

We want to design a business card that is modern and appealing using existing logo supplied

Front card
Residential Commercial Diary
RTA : AU052731
Licence L287456

Back card
Warren Kostig
Director
0491 357 208
info@frostlinerefrigeration.com.au
www.frostlinerefrigeration.com.au
• Air Conditioning
• Cool Rooms & Refrigeration
• Installation
• Service & Repair
• Preventative Maintenance

We offer 24/7 emergency service

```html
<!DOCTYPE html>
<html lang="en">
<head>
<meta charset="utf-8">
<title>Frostline Business Card</title>
<link href="https://fonts.googleapis.com/css2?family=Arimo:wght@400;700&display=swap" rel="stylesheet">
<style>
  :root {
    --page: #e9e9ec;
    --card: #060507;
    --purple: #9b6fc4;
    --purple-deep: #6b3fa0;
    --ice: #d7e3f8;
    --white: #f4f4f6;
    --muted: #d8d8dc;
  }
  * { margin: 0; padding: 0; box-sizing: border-box; }
  html, body {
    width: 1200px; height: 900px; overflow: hidden;
    background: var(--page);
    font-family: "Arimo", Arial, sans-serif;
  }
  .card {
    position: absolute; left: 250px;
    width: 700px; height: 400px;
    background: var(--card);
    border-radius: 28px;
    overflow: hidden;
    box-shadow: 0 12px 30px rgba(0,0,0,.25);
  }
  .card--contact { top: 40px; }
  .card--brand { top: 460px; }
  .card__band { position: absolute; inset: 0; width: 700px; height: 400px; }
  .brand { position: absolute; display: flex; align-items: center; gap: 12px; }
  .brand__dot { width: 30px; height: 30px; border-radius: 50%; background: var(--purple); }
  .brand__name { color: var(--white); font-weight: 700; letter-spacing: 2px; }
  .card--contact .brand { left: 44px; top: 52px; }
  .card--contact .brand__name { font-size: 38px; }
  .card--brand .brand { left: 50%; top: 160px; transform: translateX(-50%); }
  .card--brand .brand__dot { width: 44px; height: 44px; }
  .card--brand .brand__name { font-size: 56px; }
  .person { position: absolute; left: 60px; top: 128px; }
  .person__name { color: var(--purple); font-weight: 700; font-size: 20px; letter-spacing: .5px; text-transform: uppercase; }
  .person__role { color: var(--muted); font-size: 15px; margin-top: 3px; }
  .contacts { position: absolute; left: 60px; top: 196px; list-style: none; }
  .contacts li { display: flex; align-items: center; gap: 10px; color: var(--white); font-size: 16px; margin-bottom: 9px; }
  .contacts svg { width: 16px; height: 16px; flex: none; }
  .services { position: absolute; right: 40px; top: 52px; text-align: right; list-style: none; }
  .services .services__item { color: var(--white); font-size: 16px; margin-bottom: 5px; }
  .services .services__item::after { content: " \2713"; color: var(--purple); }
  .services .services__title { color: var(--purple); font-weight: 700; font-size: 20px; margin-bottom: 6px; }
  .band-text {
    position: absolute; right: 20px; color: var(--purple-deep);
    font-weight: 700; text-align: right; white-space: nowrap;
  }
  .card--contact .band-text { bottom: 18px; font-size: 15px; }
  .card--brand .band-text { bottom: 12px; font-size: 14px; line-height: 1.35; }
</style>
</head>
<body>

<section class="card card--contact">
  <svg class="card__band" viewBox="0 0 700 400" aria-hidden="true">
    <path d="M0 390 L390 390 L412 350 L700 350 L700 400 L0 400 Z" fill="var(--ice)"/>
    <path d="M0 383 L385 383 L407 343" stroke="var(--purple-deep)" stroke-width="3" fill="none"/>
  </svg>
  <div class="brand"><span class="brand__dot"></span><span class="brand__name">FROSTLINE</span></div>
  <div class="person">
    <p class="person__name">Warren Kostig</p>
    <p class="person__role">Director</p>
  </div>
  <ul class="contacts">
    <li><svg viewBox="0 0 16 16"><path d="M3 1.5h3l1.3 3.3-1.8 1.3a8 8 0 0 0 4.4 4.4l1.3-1.8 3.3 1.3v3a1.5 1.5 0 0 1-1.6 1.5A13 13 0 0 1 1.5 3.1 1.5 1.5 0 0 1 3 1.5z" fill="var(--purple)"/></svg>0491 357 208</li>
    <li><svg viewBox="0 0 16 16"><rect x="1" y="3" width="14" height="10" rx="1" fill="var(--purple)"/><path d="M1.5 3.5 8 9l6.5-5.5" stroke="var(--card)" stroke-width="1.3" fill="none"/></svg>info@frostlinerefrigeration.com.au</li>
    <li><svg viewBox="0 0 16 16" fill="none" stroke="var(--purple)" stroke-width="1.3"><circle cx="8" cy="8" r="6.5"/><ellipse cx="8" cy="8" rx="3" ry="6.5"/><path d="M1.5 8h13M2.5 4.5h11M2.5 11.5h11"/></svg>www.frostlinerefrigeration.com.au</li>
  </ul>
  <ul class="services">
    <li class="services__title">Our Services</li>
    <li class="services__item">Air Conditioning</li>
    <li class="services__item">Cool Rooms &amp; Refrigeration</li>
    <li class="services__item">Installation</li>
    <li class="services__item">Service &amp; Repair</li>
    <li class="services__item">Preventative Maintenance</li>
  </ul>
  <p class="band-text">We Offer 24/7 Emergency Service</p>
</section>

<section class="card card--brand">
  <svg class="card__band" viewBox="0 0 700 400" aria-hidden="true">
    <path d="M0 390 L370 390 L395 330 L700 330 L700 400 L0 400 Z" fill="var(--ice)"/>
    <path d="M0 383 L365 383 L390 323" stroke="var(--purple-deep)" stroke-width="3" fill="none"/>
  </svg>
  <div class="brand"><span class="brand__dot"></span><span class="brand__name">FROSTLINE</span></div>
  <p class="band-text">Residential Commercial Diary<br>RTA : AU052731 | Licence L287456</p>
</section>

</body>
</html>
```